Flyer
Zielgruppe
Ich bin eine professionelle Nail-Masterin . Meine Spezialität sind Gellacknägel. Hochprofessionelle Nägel für den Alltag bis hin zu speziellen Anlässen wie Hochzeit. Meine Arbeit steht für hochstehende Qualität die man sehen und fühlen kann. Die Zielgruppe sind Frauen die auf ihr äusseres achten und sich für spezielle Anlässe zurecht machen wollen.
Auf dem Flyer möchte ich den Start an meinem neuen Standort (Studen BE) promoten. Um meinen Kundenstamm aufzubauen werden Neukunden ein Angebot erhalten: Gellacknägel als Willkommensangebot für 49.- (SFr). Dieses Angebot ist pro Kunde nur einmalig gültig.
Terminvereinbarung per per SMS/Whatsapp 079/482 13 57 oder auf www.pirulack.ch
Aufgabenstellung
Völlig freie Hand beim Designen. Der Flyer wird per Post verteilt. Keine Falzflyer.

```html
<!DOCTYPE html>
<html lang="de">
<head>
<meta charset="utf-8">
<title>Flyer – Willkommensangebot Gellacknägel</title>
<link href="https://fonts.googleapis.com/css2?family=Bebas+Neue&family=Montserrat:wght@400;600;700&display=swap" rel="stylesheet">
<style>
  :root {
    --canvas-bg: #e8e7e3;
    --ink-black: #050403;
    --ink-brown: #6e5128;
    --gold: #d99a2b;
    --white: #ffffff;
    --frame-line: rgba(217, 154, 43, 0.55);
    --photo-light: #e9c9bf;
    --photo-dark: #7d6660;
  }
  html, body {
    margin: 0;
    padding: 0;
    width: 711px;
    height: 1200px;
    overflow: hidden;
    background: var(--canvas-bg);
  }
  .flyer {
    position: absolute;
    left: 55px;
    top: 176px;
    width: 600px;
    height: 848px;
    background: linear-gradient(180deg, var(--ink-black) 0%, var(--ink-black) 38%, #2a1f12 62%, var(--ink-brown) 100%);
    overflow: hidden;
    color: var(--white);
    text-align: center;
    font-family: "Montserrat", sans-serif;
  }
  .nail-fan {
    position: absolute;
    left: 0;
    top: 0;
    width: 600px;
    height: 320px;
  }
  .studio-name {
    position: absolute;
    left: 0;
    top: 300px;
    width: 100%;
    font-family: "Montserrat", sans-serif;
    font-weight: 700;
    font-size: 44px;
    line-height: 1;
    letter-spacing: 2px;
    color: var(--gold);
  }
  .headline {
    position: absolute;
    left: 0;
    width: 100%;
    font-family: "Bebas Neue", sans-serif;
    line-height: 1;
    margin: 0;
    font-weight: 400;
  }
  .headline-offer { top: 392px; font-size: 52px; }
  .headline-product { top: 446px; font-size: 52px; }
  .headline-for { top: 512px; font-size: 32px; }
  .price {
    position: absolute;
    top: 556px;
    left: 0;
    width: 100%;
    font-family: "Bebas Neue", sans-serif;
    font-size: 66px;
    line-height: 1;
    color: var(--gold);
  }
  .terms {
    position: absolute;
    top: 640px;
    left: 100px;
    width: 400px;
    font-size: 21px;
    line-height: 1.25;
    margin: 0;
  }
  .booking-frame {
    position: absolute;
    left: 34px;
    top: 700px;
    width: 532px;
    height: 124px;
  }
  .booking {
    position: absolute;
    top: 716px;
    left: 0;
    width: 100%;
    font-size: 22px;
    font-weight: 700;
    display: flex;
    justify-content: center;
    align-items: center;
    gap: 10px;
  }
  .booking-phone {
    display: inline-flex;
    align-items: center;
    gap: 6px;
  }
  .booking-phone svg { width: 24px; height: 24px; }
  .website {
    position: absolute;
    top: 776px;
    left: 0;
    width: 100%;
    font-size: 17px;
    font-weight: 700;
    letter-spacing: 9px;
    text-transform: uppercase;
  }
</style>
</head>
<body>
  <main class="flyer">
    <svg class="nail-fan" viewBox="0 0 600 320" role="img" aria-label="Fächer aus Fotos gepflegter Hände mit Gellacknägeln">
      <defs>
        <linearGradient id="nailPhoto" x1="0" y1="0" x2="0" y2="1">
          <stop offset="0" stop-color="var(--photo-light)"/>
          <stop offset="1" stop-color="var(--photo-dark)"/>
        </linearGradient>
      </defs>
      <g transform="translate(300 268)" fill="url(#nailPhoto)" stroke="url(#nailPhoto)" stroke-width="6" stroke-linejoin="round">
        <path class="fan-segment" transform="rotate(-82.8)" d="M -21.3 -97.7 L -52.2 -239.4 A 245 245 0 0 1 52.2 -239.4 L 21.3 -97.7 A 100 100 0 0 0 -21.3 -97.7 Z"/>
        <path class="fan-segment" transform="rotate(-55.2)" d="M -21.3 -97.7 L -52.2 -239.4 A 245 245 0 0 1 52.2 -239.4 L 21.3 -97.7 A 100 100 0 0 0 -21.3 -97.7 Z"/>
        <path class="fan-segment" transform="rotate(-27.6)" d="M -21.3 -97.7 L -52.2 -239.4 A 245 245 0 0 1 52.2 -239.4 L 21.3 -97.7 A 100 100 0 0 0 -21.3 -97.7 Z"/>
        <path class="fan-segment" d="M -21.3 -97.7 L -52.2 -239.4 A 245 245 0 0 1 52.2 -239.4 L 21.3 -97.7 A 100 100 0 0 0 -21.3 -97.7 Z"/>
        <path class="fan-segment" transform="rotate(27.6)" d="M -21.3 -97.7 L -52.2 -239.4 A 245 245 0 0 1 52.2 -239.4 L 21.3 -97.7 A 100 100 0 0 0 -21.3 -97.7 Z"/>
        <path class="fan-segment" transform="rotate(55.2)" d="M -21.3 -97.7 L -52.2 -239.4 A 245 245 0 0 1 52.2 -239.4 L 21.3 -97.7 A 100 100 0 0 0 -21.3 -97.7 Z"/>
        <path class="fan-segment" transform="rotate(82.8)" d="M -21.3 -97.7 L -52.2 -239.4 A 245 245 0 0 1 52.2 -239.4 L 21.3 -97.7 A 100 100 0 0 0 -21.3 -97.7 Z"/>
      </g>
    </svg>

    <div class="studio-name">PIRULACK</div>

    <h1 class="headline headline-offer">Willkommensangebot</h1>
    <h2 class="headline headline-product">Gellacknägel als</h2>
    <div class="headline headline-for">für</div>
    <div class="price">49.- (SFR)</div>

    <p class="terms">Dieses Angebot ist pro Kunde nur einmalig gültig.</p>

    <svg class="booking-frame" viewBox="0 0 532 124" fill="none" stroke="var(--frame-line)" stroke-width="1.5">
      <polyline points="490,2 532,2 532,80"/>
      <polyline points="0,36 0,124 400,124"/>
    </svg>

    <div class="booking">
      <span class="booking-label">Terminvereinbarung</span>
      <span class="booking-phone">
        <svg viewBox="0 0 24 24" fill="none" stroke="var(--gold)" stroke-width="2" stroke-linecap="round" stroke-linejoin="round" aria-hidden="true">
          <circle cx="12" cy="12" r="10"/>
          <path d="M8.5 7.5c0 4.5 3.5 8 8 8l1-1.8-2.3-1.2-1 1c-1.5-.6-2.7-1.8-3.3-3.3l1-1-1.2-2.3z"/>
        </svg>
        079/482 13 57
      </span>
    </div>

    <div class="website">www.pirulack.ch</div>
  </main>
</body>
</html>
```